Folder Design: Vantra Mobile Diagnostics

Need a folder designed for a Vantra Mobile Diagnostics. Folder needs to be very professional and will be used to hold brochure, contract and business card of business. Logos of the company are attached.

Industry/Entity Type

Healthcare

```html
<!DOCTYPE html>
<html lang="en">
<head>
<meta charset="utf-8">
<title>Vantra Mobile Diagnostics – Folder</title>
<link rel="stylesheet" href="https://fonts.googleapis.com/css2?family=Cinzel:wght@400;600&display=swap">
<style>
  :root {
    --page-bg: #efedea;
    --navy: #06162b;
    --navy-deep: #030d1c;
    --brand-blue: #5b9be6;
    --brand-blue-light: #a9ccf5;
    --paper: #f7f7f6;
    --paper-shade: #e9e9e8;
    --ink: #1c2230;
    --watermark: #e2e2e2;
  }
  * { margin: 0; padding: 0; box-sizing: border-box; }
  html, body { width: 1200px; height: 2572px; overflow: hidden; }
  body {
    background: var(--page-bg);
    font-family: "Cinzel", serif;
    position: relative;
  }
  .sheet {
    position: absolute;
    width: 540px;
    height: 760px;
    box-shadow: 0 14px 30px rgba(0,0,0,.18);
  }

  /* Front cover */
  .cover { left: 40px; top: 110px; background: linear-gradient(160deg, #0c2038, var(--navy) 40%, var(--navy-deep)); }
  .brand-mark {
    display: flex; align-items: center; gap: 10px;
    color: var(--brand-blue);
    font-family: "Cinzel", serif; font-weight: 400;
    letter-spacing: 3px;
  }
  .brand-mark .dot {
    width: 14px; height: 14px; border-radius: 50%;
    background: var(--brand-blue);
  }
  .cover .brand-mark { position: absolute; top: 60px; left: 50%; transform: translateX(-50%); font-size: 22px; }
  .cover .title {
    position: absolute; top: 118px; left: 0; right: 0;
    text-align: center; color: var(--brand-blue-light);
    font-size: 26px; letter-spacing: 2px;
  }
  .cover .emblem {
    position: absolute; left: 90px; top: 200px; width: 360px; height: 560px;
    border-radius: 180px 180px 0 0;
    background: radial-gradient(circle at 50% 30%, var(--brand-blue-light), var(--brand-blue) 45%, rgba(91,155,230,.15) 80%);
  }

  /* Letterhead */
  .letterhead { left: 620px; top: 110px; background: var(--paper); }
  .letterhead .watermark {
    position: absolute; left: 110px; top: 50px; width: 320px; height: 470px;
    border-radius: 160px 160px 40px 40px;
    background: linear-gradient(180deg, var(--watermark), rgba(226,226,226,.25));
  }
  .letterhead .brand-mark { position: absolute; left: 50%; top: 580px; transform: translateX(-50%); font-size: 18px; }
  .letterhead .web {
    position: absolute; left: 0; right: 0; top: 660px;
    text-align: center; color: var(--ink); font-size: 20px; letter-spacing: 5px;
  }
  .letterhead .edge { position: absolute; left: 0; right: 0; bottom: 0; height: 6px; background: var(--brand-blue); }

  /* Inside spread */
  .spread { position: absolute; left: 60px; top: 980px; width: 1080px; height: 760px; box-shadow: 0 14px 30px rgba(0,0,0,.18); }
  .spread .panel { position: absolute; top: 0; width: 540px; height: 760px; }
  .spread .panel-left { left: 0; background: var(--paper); }
  .spread .panel-right { left: 540px; background: var(--paper-shade); border-left: 1px solid #d6d6d6; }
  .pocket { position: absolute; left: 0; bottom: 0; width: 540px; height: 300px; }
  .pocket .brand-mark { position: absolute; left: 50%; top: 120px; transform: translateX(-50%); font-size: 20px; }
  .pocket .tagline {
    position: absolute; left: 0; right: 0; top: 165px; text-align: center;
    color: var(--brand-blue); font-size: 12px; letter-spacing: 2px;
  }

  /* Business cards */
  .card {
    position: absolute; top: 1860px; width: 500px; height: 290px;
    box-shadow: 0 10px 22px rgba(0,0,0,.18);
  }
  .card-front { left: 60px; background: var(--navy); }
  .card-back { left: 640px; background: var(--navy); }
  .card-front .brand-mark { position: absolute; left: 50%; top: 110px; transform: translateX(-50%); font-size: 26px; }
  .card-front .tagline {
    position: absolute; left: 0; right: 0; top: 160px; text-align: center;
    color: var(--brand-blue); font-size: 13px; letter-spacing: 2px;
  }
  .card-back .title {
    position: absolute; left: 0; right: 0; top: 120px; text-align: center;
    color: var(--brand-blue-light); font-size: 20px; letter-spacing: 2px;
  }
  .card-back .web {
    position: absolute; left: 0; right: 0; top: 165px; text-align: center;
    color: var(--brand-blue); font-size: 14px; letter-spacing: 4px;
  }
</style>
</head>
<body>

  <section class="sheet cover">
    <div class="brand-mark"><span class="dot"></span>Vantra</div>
    <h1 class="title">Vantra Mobile Diagnostics</h1>
    <div class="emblem" role="img" aria-label="Large emblem illustration: winged staff with two serpents in light blue"></div>
  </section>

  <section class="sheet letterhead">
    <div class="watermark" role="img" aria-label="Faint embossed emblem illustration"></div>
    <div class="brand-mark"><span class="dot"></span>Vantra</div>
    <p class="web">www.vantra-lab.example</p>
    <div class="edge"></div>
  </section>

  <section class="spread">
    <div class="panel panel-left">
      <div class="pocket">
        <svg width="540" height="300" viewBox="0 0 540 300" aria-hidden="true">
          <path d="M0 40 Q0 0 60 0 L440 0 Q500 0 520 40 L540 80 L540 300 L0 300 Z" fill="var(--navy)"/>
        </svg>
        <div class="brand-mark"><span class="dot"></span>Vantra</div>
        <p class="tagline">Vantra Mobile Diagnostics</p>
      </div>
    </div>
    <div class="panel panel-right">
      <div class="pocket">
        <svg width="540" height="300" viewBox="0 0 540 300" aria-hidden="true">
          <path d="M0 80 L30 30 Q50 0 100 0 L540 0 L540 300 L0 300 Z" fill="var(--navy)"/>
          <path d="M170 90 L330 90 L350 110 L350 160 L330 180 L170 180 L150 160 L150 110 Z" fill="#cfcfcf"/>
        </svg>
      </div>
    </div>
  </section>

  <section class="card card-front">
    <div class="brand-mark"><span class="dot"></span>Vantra</div>
    <p class="tagline">Vantra Mobile Diagnostics</p>
  </section>

  <section class="card card-back">
    <p class="title">Vantra Mobile Diagnostics</p>
    <p class="web">www.vantra-lab.example</p>
  </section>

</body>
</html>
```